business card letterhead envelope
Darren Holcomb Realtors
Project: business card letterhead envelope
business card letterhead envelope - Real Estate
Creative Brief
Professional
Darren Holcomb
Attorney/Broker
2817 W. Larkspur Ave Suite B7 Odessa, TX 79748
Darren@PecosPrairieHouses.com
PecosPrairieHouses.com

```html
<!DOCTYPE html>
<html lang="en">
<head>
<meta charset="utf-8">
<title>Darren Holcomb Realtors — Business Card</title>
<link href="https://fonts.googleapis.com/css2?family=Arimo:wght@400;700&display=swap" rel="stylesheet">
<style>
  :root {
    --page-bg: #e8e6e3;
    --card-white: #ffffff;
    --swoosh-grey: #a9a9a9;
    --ink-dark: #1c1c1c;
    --ink-light: #ffffff;
    --ink-soft: #e6e6e6;
    --panel-glow: #5c5c5c;
    --panel-deep: #050505;
  }
  * { margin: 0; padding: 0; box-sizing: border-box; }
  html, body {
    width: 1200px;
    height: 965px;
    overflow: hidden;
    background: var(--page-bg);
    font-family: "Arimo", Arial, sans-serif;
  }
  .business-card {
    position: absolute;
    left: 100px;
    top: 121px;
    width: 1000px;
    height: 723px;
    border-radius: 26px;
    overflow: hidden;
    box-shadow: 0 6px 18px rgba(0,0,0,0.18);
  }
  .card-art {
    position: absolute;
    inset: 0;
    width: 100%;
    height: 100%;
  }
  .brand-block {
    position: absolute;
    left: 30px;
    top: 150px;
    width: 300px;
    text-align: center;
    color: var(--ink-dark);
  }
  .brand-mark {
    display: block;
    width: 84px;
    height: 84px;
    margin: 0 auto 22px;
    border-radius: 50%;
    background: var(--ink-dark);
  }
  .brand-name {
    font-size: 27px;
    font-weight: 400;
    letter-spacing: 2px;
    text-transform: uppercase;
    line-height: 1.35;
  }
  .agent-block {
    position: absolute;
    right: 74px;
    top: 153px;
    text-align: right;
    color: var(--ink-light);
  }
  .agent-name {
    font-size: 29px;
    font-weight: 700;
  }
  .agent-title {
    font-size: 21px;
    font-weight: 700;
    margin-top: 14px;
  }
  .office-address {
    position: absolute;
    right: 81px;
    top: 372px;
    text-align: right;
    color: var(--ink-soft);
    font-size: 20px;
    line-height: 34px;
  }
  .contact-list {
    position: absolute;
    right: 40px;
    top: 478px;
    list-style: none;
    color: var(--ink-soft);
    font-size: 20px;
  }
  .contact-item {
    display: flex;
    justify-content: flex-end;
    align-items: center;
    height: 46.5px;
  }
  .contact-icon {
    width: 26px;
    height: 26px;
    margin-left: 16px;
    flex: none;
  }
</style>
</head>
<body>
  <div class="business-card">
    <svg class="card-art" viewBox="0 0 1000 723" preserveAspectRatio="none" aria-hidden="true">
      <defs>
        <radialGradient id="panelShade" cx="0.6" cy="0.42" r="0.65">
          <stop offset="0" stop-color="var(--panel-glow)"/>
          <stop offset="0.55" stop-color="#222"/>
          <stop offset="1" stop-color="var(--panel-deep)"/>
        </radialGradient>
      </defs>
      <rect class="dark-panel" width="1000" height="723" fill="url(#panelShade)"/>
      <path class="grey-swoosh" d="M0,0 H356 C420,200 452,470 432,723 H0 Z" fill="var(--swoosh-grey)"/>
      <path class="white-panel" d="M0,0 H348 C400,200 424,470 404,723 H0 Z" fill="var(--card-white)"/>
    </svg>

    <div class="brand-block">
      <span class="brand-mark"></span>
      <p class="brand-name">Darren Holcomb<br>Realtors</p>
    </div>

    <div class="agent-block">
      <p class="agent-name">Darren Holcomb</p>
      <p class="agent-title">Attorney/Broker</p>
    </div>

    <p class="office-address">2817 W. Larkspur Ave Suite B7<br>Odessa, TX 79748</p>

    <ul class="contact-list">
      <li class="contact-item">432.555.0147
        <svg class="contact-icon" viewBox="0 0 24 24"><path d="M6 3l3 0 1.5 4.5-2 1.5c1 2.5 3 4.5 5.5 5.5l1.5-2 4.5 1.5v3c0 1-1 2-2 2C10 19 5 14 4 5c0-1 1-2 2-2z" fill="#fff"/></svg>
      </li>
      <li class="contact-item">432.555.0193
        <svg class="contact-icon" viewBox="0 0 24 24"><rect x="7" y="2" width="10" height="20" rx="2" fill="none" stroke="#fff" stroke-width="2"/><rect x="9" y="5" width="6" height="9" fill="#fff"/></svg>
      </li>
      <li class="contact-item">432.555.0162
        <svg class="contact-icon" viewBox="0 0 24 24"><rect x="7" y="3" width="10" height="7" fill="#fff"/><rect x="4" y="10" width="16" height="11" rx="1.5" fill="#fff"/><rect x="7" y="13" width="10" height="2" fill="#222"/><rect x="7" y="17" width="4" height="2" fill="#222"/></svg>
      </li>
      <li class="contact-item">Darren@PecosPrairieHouses.com
        <svg class="contact-icon" viewBox="0 0 24 24"><circle cx="12" cy="12" r="3.8" fill="none" stroke="#fff" stroke-width="2.2"/><path d="M15.8 9v4.5c0 2 3.7 2 3.7-1.5A7.5 7.5 0 1 0 16 18.5" fill="none" stroke="#fff" stroke-width="2.2"/></svg>
      </li>
      <li class="contact-item">www.PecosPrairieHouses.com
        <svg class="contact-icon" viewBox="0 0 24 24"><circle cx="12" cy="12" r="9" fill="none" stroke="#fff" stroke-width="1.8"/><ellipse cx="12" cy="12" rx="4" ry="9" fill="none" stroke="#fff" stroke-width="1.6"/><path d="M3 12h18M5 7h14M5 17h14" stroke="#fff" stroke-width="1.4"/></svg>
      </li>
    </ul>
  </div>
</body>
</html>
```